Newspaper Ad for Front page strip

Kestrel Quick Credit is a micro lender operating in the Caribbean. This ad is for our Trinidad and Tobago location.
Would like to design a catchy banner ad for the front page of a daily newspaper. The ad should capture 1) that we offer unsecured loans up to $40,000. 2) customer can apply online or over the phone 3) that the process is quick.
We have included the a snapshot of our Instagram posts as well as the newspaper location and size of the ad.
We have booked this ad spot for the year so the more engaging we can make it the better. Maybe we can do a series of ads or weekly storyline . Let’s be creative.
https://www.instagram.com/kestrelquickcredit/
www.kestrelquick credit.example
Target Market(s)
Mass population.
Industry/Entity Type
Banking
Look and feel

```html
<!DOCTYPE html>
<html lang="en">
<head>
<meta charset="utf-8">
<title>Kestrel Quick Credit – Front Page Strip</title>
<link href="https://fonts.googleapis.com/css2?family=Lobster&family=Montserrat:wght@600;700;800&family=Oswald:wght@700&display=swap" rel="stylesheet">
<style>
  :root{
    --page:#e3e3e3;
    --white:#ffffff;
    --ink:#1c1c1c;
    --red:#e3322b;
    --green:#1e9a3f;
    --green-dark:#15802f;
    --yellow:#f6e33c;
    --photo-a:#c9ced6;
    --photo-b:#6c86a6;
  }
  *{margin:0;padding:0;box-sizing:border-box}
  html,body{width:1200px;height:2400px;overflow:hidden;background:var(--page)}
  .strip-ad{position:absolute;left:340px;top:60px;width:520px;height:2280px;background:var(--white);overflow:hidden;font-family:"Montserrat",sans-serif}
  .ad-shapes{position:absolute;left:0;top:0}
  .brand{position:absolute;top:78px;left:0;width:100%;display:flex;justify-content:center;align-items:center;gap:12px}
  .brand-mark{width:26px;height:26px;background:var(--red)}
  .brand-name{font-weight:700;font-size:30px;color:var(--green);letter-spacing:-0.5px}
  .headline{position:absolute;left:40px;top:175px;width:440px;font-family:"Lobster",cursive;line-height:0.9}
  .headline .line-1{display:block;font-size:150px;color:var(--ink)}
  .headline .line-2{display:block;font-size:140px;color:var(--red);text-align:right}
  .apply-btn{position:absolute;left:66px;top:484px;width:388px;height:60px;border-radius:30px;background:var(--green);color:var(--white);font-weight:700;font-size:36px;letter-spacing:2px;display:flex;align-items:center;justify-content:center;box-shadow:0 5px 0 var(--green-dark)}
  .offer{position:absolute;left:46px;top:1535px;color:var(--white);font-weight:600;font-size:35px;line-height:1.3;letter-spacing:1px}
  .amount{position:absolute;left:40px;top:1630px;font-family:"Oswald",sans-serif;font-weight:700;font-size:122px;color:var(--yellow);line-height:1;letter-spacing:-1px}
  .amount sup{font-size:70px;vertical-align:top;position:relative;top:14px}
  .benefits{position:absolute;left:48px;top:1800px;width:250px;list-style:none}
  .benefits li{position:relative;padding-left:46px;color:var(--white);font-weight:700;font-size:32px;line-height:1.25;letter-spacing:0.5px;margin-bottom:36px}
  .benefits svg{position:absolute;left:0;top:8px}
  .footer-web{position:absolute;left:0;bottom:0;width:100%;height:90px;display:flex;align-items:center;justify-content:center;gap:16px;font-weight:700;font-size:30px;color:var(--ink)}
  .social-square{width:28px;height:28px;border-radius:6px;border:3px solid var(--red)}
  .phone-brand{font-family:"Montserrat",sans-serif;font-weight:700;font-size:14px;fill:var(--green)}
  .phone-btn-text{font-family:"Montserrat",sans-serif;font-weight:700;font-size:9px;fill:var(--white)}
</style>
</head>
<body>
<div class="strip-ad">
  <svg class="ad-shapes" width="520" height="2280" viewBox="0 0 520 2280">
    <defs>
      <linearGradient id="photoTone" x1="0" y1="0" x2="0" y2="1">
        <stop offset="0" stop-color="var(--photo-a)"/>
        <stop offset="1" stop-color="var(--photo-b)"/>
      </linearGradient>
      <linearGradient id="couplePhoto" x1="0" y1="0" x2="1" y2="1">
        <stop offset="0" stop-color="#f1e6cf"/>
        <stop offset="1" stop-color="#c79a4a"/>
      </linearGradient>
    </defs>
    <rect role="img" aria-label="Photo of a smiling man in glasses giving a thumbs up and holding a phone" x="0" y="590" width="520" height="880" fill="url(#photoTone)"/>
    <polygon points="0,1040 520,1540 520,1552 0,1052" fill="var(--green)"/>
    <polygon points="0,1058 520,1558 520,1570 0,1070" fill="var(--yellow)"/>
    <polygon points="0,1070 520,1570 520,1660 0,1180" fill="var(--red)"/>
    <polygon points="0,1180 520,1660 520,2190 0,2190" fill="var(--green)"/>
    <circle cx="208" cy="1345" r="172" fill="var(--white)"/>
    <circle cx="208" cy="1345" r="166" fill="var(--red)"/>
    <circle role="img" aria-label="Photo of a couple reviewing loan papers at home" cx="208" cy="1345" r="156" fill="url(#couplePhoto)"/>
    <g class="phone">
      <rect x="300" y="1800" width="182" height="372" rx="24" fill="#d7d9dc"/>
      <rect x="306" y="1806" width="170" height="360" rx="20" fill="var(--white)"/>
      <rect x="370" y="1818" width="42" height="5" rx="2.5" fill="#c4c6c9"/>
      <text x="391" y="1996" text-anchor="middle" class="phone-brand">Kestrel Quick Credit</text>
      <rect x="341" y="2008" width="100" height="14" rx="7" fill="var(--green)"/>
      <text x="391" y="2018" text-anchor="middle" class="phone-btn-text">APPLY NOW</text>
    </g>
  </svg>

  <div class="brand"><span class="brand-mark"></span><span class="brand-name">Kestrel Quick Credit</span></div>

  <h1 class="headline"><span class="line-1">In your</span><span class="line-2">world</span></h1>

  <div class="apply-btn">APPLY NOW</div>

  <p class="offer">That we offer<br>unsecured loans up to</p>
  <p class="amount"><sup>$</sup>40,000</p>

  <ul class="benefits">
    <li><svg width="24" height="24" viewBox="0 0 24 24"><circle cx="12" cy="12" r="12" fill="var(--yellow)"/><path d="M6.5 12.5l3.5 3.5 7-7.5" stroke="var(--green)" stroke-width="3" fill="none"/></svg>Customer can apply online or over the phone</li>
    <li><svg width="24" height="24" viewBox="0 0 24 24"><circle cx="12" cy="12" r="12" fill="var(--yellow)"/><path d="M6.5 12.5l3.5 3.5 7-7.5" stroke="var(--green)" stroke-width="3" fill="none"/></svg>That the process is quick.</li>
  </ul>

  <div class="footer-web"><span>www.tt.kestrelquick.example</span><span class="social-square"></span></div>
</div>
</body>
</html>
```